Poster design for Non-Profit Harbor Pathways

Harbor Pathways is a not-for-profit providing disability services to improve the lives of the people we serve. We are holding an internal convention with staff focusing on improving what we already do well. The title of the event and ongoing effort will be ‘Ventus Aperta’, with a sub-title of ‘Focusing on our Strengths’.

Target Market(s)

Our employees

Industry/Entity Type

Non Profit

Font styles to use
Serif

Requirements
Must have
• • Be A0 size
• • Include the title ‘Ventus Aperta’
• • Include the sub-title ‘ Focusing on our Strengths’
• • Include the Harbor Pathways Logo
• • A colour scheme that ties in to our logo
Nice to have
• A bold, minimalist design with clear lettering. Refer to the files inspiration 1 and 2. Also I will upload a brochure we had designed recently. Please ignore our website for design features as it is outdated.
Should not have
• Too many photos.

```html
<!DOCTYPE html>
<html lang="en">
<head>
<meta charset="utf-8">
<title>Harbor Pathways – Ventus Aperta</title>
<link href="https://fonts.googleapis.com/css2?family=Cinzel:wght@600;700&family=Playfair+Display:ital,wght@0,500;0,700;1,700&display=swap" rel="stylesheet">
<style>
  :root {
    --purple-deep: #4a1a78;
    --purple: #6d2a8f;
    --violet: #8a2f9e;
    --magenta: #c2249a;
    --pink: #e0389a;
    --white: #ffffff;
    --rule: #6a5a7a;
  }
  html, body {
    margin: 0;
    padding: 0;
    overflow: hidden;
    background: var(--white);
  }
  .poster {
    position: relative;
    width: 849px;
    height: 1200px;
    overflow: hidden;
    background: var(--white);
    font-family: "Playfair Display", Georgia, serif;
  }
  .poster__shapes {
    position: absolute;
    inset: 0;
  }
  .brand {
    position: absolute;
    top: 28px;
    left: 300px;
    display: flex;
    align-items: center;
    gap: 16px;
    color: var(--white);
  }
  .brand__dot {
    width: 62px;
    height: 62px;
    border-radius: 50%;
    background: var(--white);
    opacity: 0.9;
  }
  .brand__name {
    font-family: "Playfair Display", Georgia, serif;
    font-weight: 700;
    font-size: 34px;
    line-height: 1;
    letter-spacing: 1px;
    text-transform: uppercase;
  }
  .headline {
    position: absolute;
    left: 0;
    width: 100%;
    text-align: center;
    margin: 0;
    color: var(--purple);
    line-height: 1;
  }
  .title-main {
    top: 200px;
    font-size: 140px;
    font-weight: 700;
    color: var(--violet);
  }
  .title-sub {
    top: 318px;
    font-size: 122px;
    font-style: italic;
    font-weight: 700;
    color: var(--purple);
  }
  .ornament {
    position: absolute;
    top: 440px;
    left: 250px;
    width: 350px;
    height: 46px;
    border-radius: 23px;
    background: linear-gradient(90deg, rgba(138,47,158,0.15), rgba(138,47,158,0.55), rgba(138,47,158,0.15));
  }
  .subtitle {
    position: absolute;
    left: 0;
    width: 100%;
    text-align: center;
    margin: 0;
    line-height: 1;
  }
  .subtitle__first {
    top: 518px;
    font-family: "Playfair Display", Georgia, serif;
    font-weight: 500;
    font-size: 112px;
    letter-spacing: 12px;
    color: var(--violet);
  }
  .subtitle__middle {
    top: 652px;
    font-family: "Cinzel", Georgia, serif;
    font-weight: 600;
    font-size: 80px;
    color: var(--purple-deep);
  }
  .subtitle__last {
    top: 748px;
    font-family: "Cinzel", Georgia, serif;
    font-weight: 700;
    font-size: 108px;
    color: var(--magenta);
  }
  .values {
    position: absolute;
    left: 0;
    bottom: 26px;
    width: 100%;
    text-align: center;
    margin: 0;
    color: var(--white);
    font-family: "Playfair Display", Georgia, serif;
    font-weight: 700;
    font-style: italic;
    font-size: 34px;
    word-spacing: 4px;
  }
</style>
</head>
<body>
  <main class="poster">
    <svg class="poster__shapes" width="849" height="1200" viewBox="0 0 849 1200" aria-hidden="true">
      <defs>
        <linearGradient id="header-fill" x1="0" y1="0" x2="1" y2="1">
          <stop offset="0" stop-color="#6a2a96"/>
          <stop offset="0.6" stop-color="#9a2fa8"/>
          <stop offset="1" stop-color="#c23aa8"/>
        </linearGradient>
        <linearGradient id="footer-fill" x1="0" y1="0" x2="1" y2="1">
          <stop offset="0" stop-color="#e0389a"/>
          <stop offset="0.45" stop-color="#a82ea6"/>
          <stop offset="1" stop-color="#4a1a78"/>
        </linearGradient>
      </defs>
      <polygon class="header-band" points="0,0 849,0 849,115 0,200" fill="url(#header-fill)"/>
      <line class="divider-rule" x1="0" y1="372" x2="849" y2="334" stroke="#6a5a7a" stroke-width="2"/>
      <polygon class="footer-band" points="0,852 849,940 849,1200 0,1200" fill="url(#footer-fill)"/>
    </svg>

    <header class="brand">
      <span class="brand__dot"></span>
      <span class="brand__name">Harbor<br>Pathways</span>
    </header>

    <h1 class="headline title-main">Ventus</h1>
    <h1 class="headline title-sub">Aperta</h1>

    <div class="ornament" role="img" aria-label="Decorative purple flourish divider"></div>

    <h2 class="subtitle subtitle__first">Focusing</h2>
    <h2 class="subtitle subtitle__middle">On Our</h2>
    <h2 class="subtitle subtitle__last">STRENGTHS!</h2>

    <p class="values">* WE Listen * WE Plan * WE Do * WE Care</p>
  </main>
</body>
</html>
```